I need a book cover for a professional training book. I specialize in teaching financial professionals and insurance agents how to prospect and schedule first appointments by phone. My professional nickname is The DialMentor. I have been doing this training for over 30 years and am known to the industry. This book addresses the challenges the smartphone has created for the financial industry, which is a high trust profession. People are digitalizing every interaction but cannot do that with their financial advisor, so prospecting new clients has to adapt to the new world. I also address the changes the pandemic has added to this very old industry.
Please include my legal name : Merle T. Ashworth, and my nickname, The DialMentor (no spaces) on the cover
Updates

Title of my book is Booking Meetings in the Pocket Device Era. It is about how to prospect and set appointments by phone. My full name is Merle T. Ashworth and I want my branded (nickname) The DialMentor underneath it on the cover. If you want to use my logo, you can lift it from my website: www.dialmentor-example.com. My book is a training book for financial advisors, mostly newer ones. I have a built in market for a few reasons: 1. I have been training financial professionals for 30+ years. 2. I am well known in the industry. 3. Clients who hire me will buy 20 or more books at a time for their rookies. 4. I am promoting myself on WorkNexus and several professional friends tell others to buy my book. The book will not be on bookshelves in airports. It is not a novel. The industry I work in is more serious than silly. I already have a published book Current Calendar Building, Lead Finding and Calling for Money Managers. You can see it on Bookvale. I'd like to use a SIMILAR font on this book (or the same one). I do not want a purple book cover since it will create confusion between the two books. My audience runs from 22 year-olds fresh out of college to people over 60. It is not for one generation but all. I teach men, women, and all ethnicities, so I am concerned about a photo of someone holding a smartphone with obviously male/female hands. A good image will tell the story of getting appointments by phone without knowing the title. I will respond to your designs and messages quickly as I hope to make a decision soon. The book is already written and my editor is awaiting the artwork from you. Thank you in advance for accepting my project. Merle

Target Market(s)

Financial Advisors and Insurance Agents, Trainers and Manager in the financial services industry

Industry/Entity Type

Financial services, insurance

Requirements
Must have
• Clarity in the design
Should not have
• Illistrations or anything childish. This is a serious business but I don't want the cover to be boring and dour.

```html
<!DOCTYPE html>
<html lang="en">
<head>
<meta charset="utf-8">
<title>Booking Meetings in the Pocket Device Era — Cover Wrap</title>
<link rel="stylesheet" href="https://fonts.googleapis.com/css2?family=Old+Standard+TT:ital,wght@0,400;0,700;1,400&family=Lato:wght@400;700&display=swap">
<style>
  :root {
    --page: #e8e6e2;
    --teal-deep: #031c20;
    --teal-mid: #0b4d52;
    --teal-glow: #1a8f92;
    --cyan: #19e6e6;
    --white: #ffffff;
    --soft-white: #f1f5f5;
    --photo-a: #c98a62;
    --photo-b: #efe6dc;
    --device-a: #27d4cf;
    --device-b: #0f7f9a;
  }
  * { margin: 0; padding: 0; box-sizing: border-box; }
  html, body { width: 1200px; height: 966px; overflow: hidden; background: var(--page); }
  .cover-wrap {
    position: absolute; left: 0; top: 50px; width: 1200px; height: 866px;
    background:
      radial-gradient(ellipse 360px 420px at 925px 470px, var(--teal-glow) 0%, transparent 75%),
      radial-gradient(ellipse 360px 380px at 287px 360px, #157c80 0%, transparent 75%),
      linear-gradient(180deg, var(--teal-mid) 0%, var(--teal-deep) 100%);
    color: var(--white);
    overflow: hidden;
  }
  .serif { font-family: "Old Standard TT", "Century Schoolbook", serif; }
  .sans { font-family: "Lato", Arial, sans-serif; }

  /* Back cover */
  .back { position: absolute; left: 0; top: 0; width: 573px; height: 866px; }
  .back-title { position: absolute; top: 28px; left: 0; width: 573px; text-align: center; }
  .back-title .main { display: block; font-size: 34px; color: var(--cyan); letter-spacing: 0.5px; line-height: 40px; }
  .back-title .sub { display: block; font-size: 31px; line-height: 36px; }
  .back-title .sub small { font-size: 19px; }
  .blurb { position: absolute; left: 57px; width: 458px; font-size: 17.5px; line-height: 22px; text-align: justify; text-align-last: center; }
  .blurb::first-letter { font-size: 26px; font-weight: 700; }
  .blurb-one { top: 135px; }
  .blurb-two { top: 438px; }
  .author-photo { position: absolute; left: 34px; top: 578px; width: 155px; height: 203px;
    background: linear-gradient(160deg, var(--photo-a) 0%, var(--photo-b) 100%); }
  .bio { position: absolute; left: 208px; top: 592px; width: 320px; font-size: 14.5px; line-height: 19px; text-align: justify; text-align-last: center; }
  .bio::first-letter { font-size: 20px; }
  .brand-mark { position: absolute; left: 40px; top: 800px; font-size: 18px; color: var(--white); }

  /* Spine */
  .spine { position: absolute; left: 573px; top: 0; width: 62px; height: 866px; }
  .spine-title, .spine-author { position: absolute; left: 0; width: 62px; writing-mode: vertical-rl; display: flex; align-items: center; justify-content: flex-start; }
  .spine-title { top: 34px; font-size: 31px; color: var(--cyan); }
  .spine-author { top: 555px; font-size: 24px; font-weight: 700; }

  /* Front cover */
  .front { position: absolute; left: 635px; top: 0; width: 565px; height: 866px; text-align: center; }
  .front-title { position: absolute; top: 22px; left: 0; width: 565px; }
  .front-title .line-big { display: block; font-size: 92px; line-height: 96px; color: var(--cyan); }
  .front-title .line-mid { display: block; font-size: 56px; line-height: 54px; color: var(--cyan); }
  .front-title .line-join { display: flex; align-items: center; justify-content: center; gap: 16px; font-size: 30px; line-height: 36px; margin-top: 2px; }
  .front-title .line-join::before, .front-title .line-join::after { content: ""; width: 56px; height: 1.5px; background: var(--white); }
  .front-title .line-end { display: block; font-size: 47px; line-height: 50px; }
  .device-art { position: absolute; left: 188px; top: 285px; width: 215px; height: 415px; border-radius: 38px;
    transform: rotate(-20deg);
    background: linear-gradient(170deg, var(--device-a) 0%, var(--device-b) 100%);
    box-shadow: 0 0 28px 6px rgba(25, 230, 230, 0.55); }
  .front-author { position: absolute; top: 735px; left: 0; width: 565px; font-size: 38px; font-weight: 700; letter-spacing: 0.5px; }
  .front-brand { position: absolute; top: 790px; left: 0; width: 565px; font-size: 24px; font-style: italic; }
</style>
</head>
<body>
  <main class="cover-wrap">
    <section class="back">
      <h2 class="back-title serif">
        <span class="main">BOOKING MEETINGS</span>
        <span class="sub"><small>in the</small> pocket device era</span>
      </h2>
      <p class="blurb blurb-one sans">Lorem ipsum dolor sit amet, consectetur adipiscing elit. Fusce ut porttitor elit. Integer auctor diam eros, id rhoncus turpis congue in. Phasellus vel lacus nec nisi bibendum sagittis laoreet ac leo. Suspendisse in sodales ex. In hac habitasse platea dictumst. Vestibulum ante ipsum primis in faucibus orci luctus et ultrices posuere cubilia curae; Phasellus eget mattis diam, nec volutpat lectus. Phasellus massa tortor, volutpat sed volutpat quis, volutpat eget ligula. Nullam efficitur facilisis sapien congue sodales. Vestibulum quis lectus orci. Donec at urna id odio elementum varius ut sed lectus. Curabitur congue sollicitudin quam, eget commodo neque dignissim.</p>
      <p class="blurb blurb-two sans">Phasellus eget aliquet felis, ut auctor ante. Nunc ut nisl vitae magna luctus congue. Proin justo eros, ultrices at luctus vitae, molestie a augue. Donec dapibus, augue a sollicitudin auctor, dui ipsum vestibulum nisi, ut gravida neque nibh a eros. Nunc sed magna condimentum, sollicitudin ex quis, vulputate nisl.</p>
      <div class="author-photo" role="img" aria-label="Author portrait photograph"></div>
      <p class="bio sans">Quisque ut semper leo. Pellentesque semper purus ac urna gravida, a ultrices eros euismod. Duis congue sem a purus mattis fermentum. Nulla id sem ultrices, faucibus eros et, condimentum orci.</p>
      <p class="brand-mark serif">The DialMentor</p>
    </section>

    <section class="spine">
      <p class="spine-title serif">BOOKING MEETINGS</p>
      <p class="spine-author serif">MERLE T. ASHWORTH</p>
    </section>

    <section class="front">
      <h1 class="front-title serif">
        <span class="line-big">BOOKING</span>
        <span class="line-mid">MEETINGS</span>
        <span class="line-join">in the</span>
        <span class="line-end">pocket device era</span>
      </h1>
      <div class="device-art" role="img" aria-label="Glowing smartphone showing an incoming call from the author"></div>
      <p class="front-author serif">MERLE T. ASHWORTH</p>
      <p class="front-brand serif">THE DIALMENTOR</p>
    </section>
  </main>
</body>
</html>
```